Design Book Cover for PhD Thesis on Cryptanalysis

I need a book cover design (front, back & spine) for my PhD thesis called "Pathways through Lattice Ciphers and Their Uses".
Author: Joost Verhagel
Keywords: cryptanalysis, digital fingerprint, digital signature, digital certificate, collision of fingerprint/signature, bit-difference.
The finished book will have dimensions 17cm by 24cm by ?cm.
The (flat-)spine thickness is yet unknown, but will probably be about 1cm.
The cover design thus needs from left-to-right:
- a back of 17cm by 24cm
- in between a spine of about 1cm by 24cm
- a front of 17cm by 24cm
Around this design a 3mm bleeding/cutoff edge is needed
(leading to a total height of 24.6 cm and total width of 35.6cm).
The spine-fold is located 7mm from the spine on the front and back cover,
so the title etc. should be removed at least 1cm from the spine.
Below I will provide a description of my biggest results in my thesis and try to give some idea of the techniques used, which may help you for inspiration.
As you will read below, cryptanalysis comes close to "hacking".
However, cryptanalysis involves much more mathematics, and our goal is to provide recommendations which cryptographic standards are (un)safe to use.
So I would prefer a cover design that generally "feels" more as cryptanalysis than "hacking".
The biggest result in my thesis is the following.
Secure websites are secured using digital certificates.
These digital certificates contain the web domain name and the server's public-key and are digitally signed by a Certificate Authority (a company/government that only signs if the public-key really belongs to the owner of the web domain).
Only a few hundred Certification Authorities are trusted in web browsers and these are publically available.
Any digital certificate signed by such a Certification Authority is considered legitimate.
To fake a secure website you thus have to get a certificate containing your public-key in combination with the target domain name signed by a Certification Authority.
Our team was able to construct a rogue sub-Certification Authority, i.e.,
a Certification Authority that is authorized by one of the publicly known Certification Authorities.
Using our rogue Certification Authority we can thus create digital certificates at will for any secure website containing our public-key.
More detailed information is available at
http://www.dep.kvl.nl/trellisbox/side-ab/
An idea of the techniques in my thesis:
I look at the internal computation of a digital signature for a certificate at bit-level and compare two such computations.
A difference between two certificates will lead to differences between the two internal computations of their digital signatures and finally to two different signatures.
However, we actively adapt the certificates to control the flow of these internal differences until we find two different certificates that actually result in the same digital signature, this is called a _collision_.
Evidently, my thesis is very technical and I have tried here to provide a short description.
You can always contact me for questions and/or more detailed explanations.
Project Deadline Extended
Reason: Almost all designs focus on the very general topic of digital security (digital fingerprint, etc).
I am looking more for a design that reflects more on the topic of the thesis: attacks on hash functions.
Several ideas have already been given in the brief and discussion.
Since the old deadline is already tomorrow, I am extend it.

```html
<!DOCTYPE html>
<html lang="en">
<head>
<meta charset="utf-8">
<title>Pathways through Lattice Ciphers and Their Uses — Cover</title>
<link rel="stylesheet" href="https://fonts.googleapis.com/css2?family=Silkscreen:wght@400;700&family=Lato:wght@400&display=swap">
<style>
  :root {
    --paper: #ffffff;
    --ink: #000000;
    --shade-light: #c9b6a3;
    --shade-mid: #6b4a33;
    --shade-dark: #1a120d;
    --shade-warm: #b07a3c;
  }
  html, body {
    margin: 0;
    padding: 0;
    width: 1200px;
    height: 823px;
    overflow: hidden;
    background: var(--paper);
  }
  .cover {
    display: block;
    width: 1200px;
    height: 823px;
  }
  .pixel-type {
    font-family: "Silkscreen", "Courier New", monospace;
    font-weight: 700;
    fill: var(--ink);
  }
  .series-line {
    font-family: "Lato", "Helvetica Neue", sans-serif;
    font-size: 11px;
    letter-spacing: 1px;
    fill: var(--ink);
  }
  .byline {
    font-family: "Lato", "Helvetica Neue", sans-serif;
    font-size: 10px;
    letter-spacing: 1.2px;
    fill: var(--ink);
  }
  .front-author {
    font-family: "Lato", "Helvetica Neue", sans-serif;
    font-size: 24px;
    letter-spacing: 3px;
    fill: var(--ink);
  }
</style>
</head>
<body>
<svg class="cover" viewBox="0 0 1200 823" xmlns="http://www.w3.org/2000/svg">
  <defs>
    <linearGradient id="dissolve-tone" x1="0" y1="0" x2="0" y2="1">
      <stop offset="0" stop-color="#ffffff"/>
      <stop offset="0.18" stop-color="var(--shade-light)"/>
      <stop offset="0.45" stop-color="var(--shade-dark)"/>
      <stop offset="0.75" stop-color="var(--shade-mid)"/>
      <stop offset="0.92" stop-color="var(--shade-warm)"/>
      <stop offset="1" stop-color="#ffffff"/>
    </linearGradient>
    <linearGradient id="spine-speck" x1="0" y1="0" x2="0" y2="1">
      <stop offset="0" stop-color="var(--shade-dark)"/>
      <stop offset="1" stop-color="var(--shade-light)"/>
    </linearGradient>
  </defs>

  <rect class="paper" width="1200" height="823" fill="var(--paper)"/>

  <!-- back cover -->
  <g class="back-cover">
    <text class="series-line" x="200" y="369" textLength="175" lengthAdjust="spacingAndGlyphs">PhD Thesis on Cryptanalysis</text>
    <text class="pixel-type" x="200" y="391" font-size="17" textLength="175" lengthAdjust="spacingAndGlyphs">Pathways through</text>
    <text class="pixel-type" x="200" y="410" font-size="14" textLength="175" lengthAdjust="spacingAndGlyphs">Lattice Ciphers</text>
    <text class="pixel-type" x="200" y="428" font-size="12" textLength="175" lengthAdjust="spacingAndGlyphs">and Their Uses</text>
    <text class="byline" x="377" y="448" text-anchor="end">by Joost Verhagel</text>
  </g>

  <!-- spine -->
  <g class="spine">
    <rect class="spine-speckle-top" x="573" y="0" width="32" height="76" fill="url(#spine-speck)" opacity="0.85" role="img" aria-label="Scattered pixel squares in brown and black"/>
    <text class="pixel-type" transform="translate(582 95) rotate(90)" font-size="17" textLength="620" lengthAdjust="spacingAndGlyphs">Pathways through Lattice Ciphers and Their Uses</text>
    <rect class="spine-speckle-bottom" x="573" y="748" width="32" height="75" fill="url(#spine-speck)" opacity="0.85" role="img" aria-label="Scattered pixel squares in brown and black"/>
  </g>

  <!-- front cover -->
  <g class="front-cover">
    <text class="pixel-type" x="748" y="118" font-size="40" textLength="294" lengthAdjust="spacingAndGlyphs">Pathways through</text>
    <text class="pixel-type" x="748" y="148" font-size="28" textLength="294" lengthAdjust="spacingAndGlyphs">Lattice Ciphers</text>
    <text class="pixel-type" x="748" y="178" font-size="22" textLength="294" lengthAdjust="spacingAndGlyphs">and Their Uses</text>

    <rect class="dissolve-artwork" x="748" y="210" width="294" height="470" fill="url(#dissolve-tone)" role="img" aria-label="Photographic portrait in warm brown tones breaking up into scattered pixel squares toward the top"/>

    <text class="front-author" x="896" y="778" text-anchor="middle">Joost Verhagel</text>
  </g>
</svg>
</body>
</html>
```